Funeral Comparison Website Needs Designer For WireFrame Mock Up (That we've already done)

This should be a pretty quick design project. It's a single page based on a wireframe mockup we did.
Our site (restfulpathway.example) helps people find and compare funeral homes and cemeteries. Our site hasn't been redesigned since we launched in 2008, so it is fairly dated, and we've seen new competitors pop-up in the past year so we need to come up with a fresh redeisgn. We need someone to take our mockup and work their magic with it. As I mentioned this is a single page based on our wireframe mockup.
Please see attached mockup and logo.
Look and feel
Each slider illustrates characteristics of the customer's brand and the style your logo design should communicate.

```html
<!DOCTYPE html>
<html lang="en">
<head>
<meta charset="utf-8">
<title>RestfulPathway – Request Funeral Quotes</title>
<link rel="stylesheet" href="https://fonts.googleapis.com/css2?family=Mulish:ital,wght@0,300;0,400;0,600;0,700;1,400&family=Arimo:ital,wght@0,400;0,700;1,400&display=swap">
<style>
:root{
  --bar-blue:#5b76a3;
  --footer-navy:#2f3b58;
  --title-blue:#2b7ca9;
  --green:#7fb628;
  --green-dark:#5f9a18;
  --link-green:#86b51f;
  --mist:#e6ecec;
  --ink:#3e4a5c;
  --muted:#5d6778;
  --rule:#c8d0d4;
  --white:#ffffff;
}
*{box-sizing:border-box;margin:0;padding:0}
html,body{width:1200px;height:1110px;overflow:hidden;background:var(--white)}
body{position:relative;font-family:"Arimo",Arial,sans-serif;color:var(--ink)}
.abs{position:absolute}

/* top bar */
.top-bar{left:0;top:0;width:1200px;height:41px;background:var(--bar-blue)}
.top-nav a,.footer-nav a{position:absolute;font-size:10px;text-decoration:none;white-space:nowrap}
.top-nav a{color:var(--white);top:14px}
.phone{left:752px;top:10px;display:flex;align-items:center;gap:6px;color:var(--white);font-family:"Mulish",sans-serif;font-size:15px}
.phone-icon{width:19px;height:19px;border-radius:50%;background:#1f3550;display:flex;align-items:center;justify-content:center}
.social{width:20px;height:20px;border-radius:50%;background:#d3dcea}

/* masthead */
.arch{left:513px;top:8px;width:174px;height:60px;border-radius:87px 87px 0 0;background:var(--white);box-shadow:0 -2px 3px rgba(30,50,90,.25)}
.arch-cover{left:505px;top:41px;width:190px;height:40px;background:var(--white)}
.brand{left:0;width:1200px;top:70px;text-align:center;font-family:"Mulish",sans-serif;font-weight:700;font-size:23px;color:var(--title-blue)}
.brand-mark{display:inline-block;width:12px;height:12px;border-radius:50%;background:var(--green);margin-right:7px;vertical-align:2px}
.page-title{left:0;width:1200px;top:134px;text-align:center;font-family:"Mulish",sans-serif;font-weight:300;font-size:38px;line-height:46px;color:var(--title-blue)}
.page-subtitle{left:0;width:1200px;top:181px;text-align:center;font-family:"Mulish",sans-serif;font-weight:600;font-size:18px;line-height:22px;color:var(--green-dark)}

/* hero */
.hero-photo{left:0;top:211px;width:1200px;height:342px;
  background:radial-gradient(ellipse at 30% 35%,#6d86d8 0,transparent 38%),
             radial-gradient(ellipse at 80% 60%,#5c74cc 0,transparent 35%),
             radial-gradient(ellipse at 50% 90%,#3a5a2a 0,transparent 40%),
             linear-gradient(90deg,#5d8a2c 0,#3c4f6c 22%,#4a5fa8 50%,#3b4f70 80%,#6d8f35 100%)}
.title-panel{left:273px;top:211px;width:654px;height:17px;background:var(--white);border-radius:0 0 4px 4px;box-shadow:0 2px 4px rgba(0,0,0,.25)}
.choice{top:273px;width:204px;height:149px;padding:6px;border-radius:4px;background:rgba(255,255,255,.35);box-shadow:0 0 6px rgba(0,0,0,.3)}
.choice-face{width:100%;height:100%;border:2px solid rgba(255,255,255,.85);display:flex;align-items:center;justify-content:center;text-align:center;padding:0 14px;color:var(--white);font-family:"Mulish",sans-serif;font-weight:300;font-size:16px;line-height:1.22}
.choice-long .choice-face{background:linear-gradient(#96cc2c,#6a9f18)}
.choice-soon .choice-face{background:linear-gradient(#7fb0e4,#3f70aa)}
.choice-now .choice-face{background:linear-gradient(#9b8c8a,#6f605e)}
.or-badge{top:320px;width:54px;height:54px;border-radius:50%;background:var(--green);border:3px solid #a9d64a;display:flex;align-items:center;justify-content:center;color:var(--white);font-family:"Mulish",sans-serif;font-weight:700;font-size:11px}
.resources-tab{left:497px;top:456px;width:205px;height:34px;border-radius:4px;background:rgba(235,240,240,.75);display:flex;align-items:center;justify-content:center;font-family:"Mulish",sans-serif;font-size:13px;color:#1f3550}

/* testimonials */
.testimonial-panel{left:273px;top:525px;width:654px;height:50px;background:linear-gradient(#eef1f6,#ffffff 14px);border-radius:4px 4px 0 0;box-shadow:0 -3px 4px -2px rgba(0,0,0,.3)}
.section-title{left:0;width:1200px;top:543px;text-align:center;font-family:"Mulish",sans-serif;font-weight:400;font-size:19px;line-height:24px;color:#4d5f82}
.quote{top:580px;width:198px;font-style:italic;font-size:10.4px;line-height:16.6px;color:var(--muted)}
.quote-name{top:684px;font-size:10px;color:var(--muted)}
.quote-name b{color:var(--ink)}
.avatar{top:708px;width:56px;height:56px;border-radius:50%;background:#d6dbe7}

/* lower */
.mist-band{left:0;top:817px;width:1200px;height:222px;background:var(--mist)}
.cta{top:790px;width:204px;height:48px;border-radius:4px;display:flex;align-items:center;justify-content:space-between;padding:0 16px 0 26px;color:var(--white);font-family:"Mulish",sans-serif;font-size:14.5px;line-height:1.1;text-decoration:none;box-shadow:0 1px 2px rgba(0,0,0,.25)}
.cta-green{background:linear-gradient(#8cc51f,#6b9e16)}
.cta-blue{background:linear-gradient(#6ea2dc,#416fa9)}
.cta-taupe{background:linear-gradient(#8f807d,#6b5d5b)}
.support-bar{left:273px;top:879px;width:654px;height:34px;border-radius:4px;background:var(--bar-blue);color:var(--white);text-align:center;font-family:"Mulish",sans-serif;font-weight:400;font-size:19px;line-height:34px}
.support-col{top:925px;width:204px}
.support-col h3{font-size:12px;color:#4a5568;padding-bottom:9px;border-bottom:1px solid var(--rule)}
.support-col ul{list-style:none;margin-top:11px}
.support-col li{font-size:10px;font-weight:700;color:var(--link-green);line-height:16.6px}

/* footer */
.site-footer{left:0;top:1039px;width:1200px;height:71px;background:var(--footer-navy)}
.footer-nav a{color:var(--link-green);top:1051px;font-size:9px}
</style>
</head>
<body>

<header>
  <div class="abs top-bar"></div>
  <div class="abs arch"></div>
  <div class="abs arch-cover"></div>
  <nav class="top-nav">
    <a href="#" style="left:280px">Menu Item</a>
    <a href="#" style="left:354px">Menu Item</a>
    <a href="#" style="left:430px">Menu Item</a>
  </nav>
  <div class="abs phone">
    <span class="phone-icon">
      <svg width="11" height="11" viewBox="0 0 24 24"><path d="M6.6 10.8a15 15 0 0 0 6.6 6.6l2.2-2.2a1 1 0 0 1 1-.25 11.4 11.4 0 0 0 3.6.57 1 1 0 0 1 1 1V20a1 1 0 0 1-1 1A17 17 0 0 1 3 4a1 1 0 0 1 1-1h3.5a1 1 0 0 1 1 1c0 1.25.2 2.45.57 3.57a1 1 0 0 1-.25 1z" fill="#fff"/></svg>
    </span>
    800.555.0199
  </div>
  <span class="abs social" style="left:879px;top:10px" aria-label="Social profile"></span>
  <span class="abs social" style="left:903px;top:10px" aria-label="Social profile"></span>
  <div class="abs brand"><span class="brand-mark"></span>RestfulPathway</div>
  <h1 class="abs page-title">Request Funeral Quotes</h1>
  <p class="abs page-subtitle">Free No Obligations Price &amp; Service Quotes</p>
</header>

<section>
  <div class="abs hero-photo" role="img" aria-label="Soft-focus photograph of blue spring flowers among green leaves"></div>
  <div class="abs title-panel"></div>
  <div class="abs choice choice-long" style="left:273px"><div class="choice-face">I am planning for the long term future</div></div>
  <div class="abs choice choice-soon" style="left:497px"><div class="choice-face">I am planning for a death that will occur shortly</div></div>
  <div class="abs choice choice-now" style="left:723px"><div class="choice-face">A death has just occurred</div></div>
  <div class="abs or-badge" style="left:460px">( OR )</div>
  <div class="abs or-badge" style="left:684px">( OR )</div>
  <div class="abs resources-tab">Additional Resources</div>
  <svg class="abs" style="left:591px;top:489px" width="18" height="10"><path d="M0 0h18L9 9z" fill="rgba(235,240,240,.75)"/></svg>
</section>

<section>
  <div class="abs testimonial-panel"></div>
  <h2 class="abs section-title">Testimonials</h2>

  <p class="abs quote" style="left:288px">Lorem ipsum dolor sit amet, consectetur adipisicing elit, sed do eiusmod tempor incididunt ut labore et dolore magna aliqua. Ut enim ad minim veniam, quis nostrud exercitation ullamco laboris nisi ut aliquip ex ea commodo consequat.</p>
  <p class="abs quote-name" style="left:288px"><b>Dana Whitfield</b> | Philadelphia, PA</p>
  <div class="abs avatar" style="left:347px" role="img" aria-label="Placeholder portrait"></div>

  <p class="abs quote" style="left:506px">Excepteur sint occaecat cupidatat non proident, sunt in culpa qui officia deserunt mollit anim id est laborum. Sed perspiciatis unde omnis iste natus error sit voluptatem accusantium doloremque laudantium, totam rem aperiam.</p>
  <p class="abs quote-name" style="left:506px"><b>Owen Marsh</b> | Los Angeles, CA</p>
  <div class="abs avatar" style="left:572px" role="img" aria-label="Placeholder portrait"></div>

  <p class="abs quote" style="left:725px">Sed ut perspiciatis unde omnis iste natus error sit voluptatem accusan laudantium, totam rem aperiam, eaque ipsa quae ab illo inventore veritatis et quasi architecto beatae vitae dicta sunt explicabo. Nemo enim ipsam voluptatem quia.</p>
  <p class="abs quote-name" style="left:725px"><b>Lena Carrow</b> | Los Angeles, CA</p>
  <div class="abs avatar" style="left:797px" role="img" aria-label="Placeholder portrait"></div>
</section>

<section>
  <div class="abs mist-band"></div>
  <a href="#" class="abs cta cta-green" style="left:273px">Get started with<br>pre-planning<svg width="10" height="18"><path d="M1 1l7 8-7 8" stroke="#4d7a10" stroke-width="3" fill="none"/></svg></a>
  <a href="#" class="abs cta cta-blue" style="left:497px">Get started<svg width="10" height="18"><path d="M1 1l7 8-7 8" stroke="#2d5689" stroke-width="3" fill="none"/></svg></a>
  <a href="#" class="abs cta cta-taupe" style="left:723px">Get started<svg width="10" height="18"><path d="M1 1l7 8-7 8" stroke="#4f4341" stroke-width="3" fill="none"/></svg></a>

  <h2 class="abs support-bar">Support Centre</h2>
  <div class="abs support-col" style="left:273px">
    <h3>Questions &amp; Answers</h3>
    <ul><li>• How we help</li><li>• How this works</li><li>• Another link in here</li></ul>
  </div>
  <div class="abs support-col" style="left:499px">
    <h3>Resources</h3>
    <ul><li>• Advice</li><li>• Finances</li><li>• Planning Guides</li></ul>
  </div>
  <div class="abs support-col" style="left:724px">
    <h3>Get More Help</h3>
    <ul><li>• Learn about our certified consultant</li><li>• Another link in here</li><li>• And maybe another one</li></ul>
  </div>
</section>

<footer>
  <div class="abs site-footer"></div>
  <nav class="footer-nav">
    <a href="#" style="left:273px">Menu Item</a>
    <a href="#" style="left:348px">Menu Item</a>
    <a href="#" style="left:423px">Menu Item</a>
  </nav>
  <span class="abs social" style="left:886px;top:1046px" aria-label="Social profile"></span>
  <span class="abs social" style="left:910px;top:1046px" aria-label="Social profile"></span>
</footer>

</body>
</html>
```